Home Remodeler Needs a Website!

Single page (plus contact form) website for small home remodeling company. He's got a few pictures he'd like on the site and needs some basic text. He likes clean, simple designs and is "more traditional" in his stylistic preferences. Most of his business comes from word-of-mouth advertising and so the site is just something he needs for people to feel more comfortable with his business.

Target Market(s)

People who want to remodel their homes

Coding

Coded - Design and coding required

Number of Pages Required

2 page

Requirements
Must have
• Main page to include some or all of the attached images, contact page. Neutral colors. Old domain: brindlecoveabodes.com New domain: qm-holdings.com You can pull text from the old site or update it.
Should not have
• No loud colors/loud visual elements

```html
<!DOCTYPE html>
<html lang="en">
<head>
<meta charset="utf-8">
<title>Brindle Cove Abodes</title>
<link href="https://fonts.googleapis.com/css2?family=Amatic+SC:wght@700&family=Poppins:wght@600;700&family=Roboto:wght@300;400;500&display=swap" rel="stylesheet">
<style>
:root{
  --accent:#e8412c;
  --navy:#2b4c9a;
  --navy-dark:#233f82;
  --ink:#222222;
  --muted:#8a8a8a;
  --white:#ffffff;
  --band:#3c3f44;
}
*{margin:0;padding:0;box-sizing:border-box}
html,body{width:1200px;height:4854px;overflow:hidden}
body{position:relative;font-family:"Roboto",Arial,sans-serif;color:var(--ink);background:var(--white)}
.abs{position:absolute}
.display{font-family:"Amatic SC","Arial Narrow",sans-serif;font-weight:700;color:var(--ink);letter-spacing:1px}
.btn{position:absolute;background:var(--accent);color:var(--white);font:500 14px/1 "Roboto",sans-serif;text-transform:uppercase;display:flex;align-items:center;justify-content:center;letter-spacing:.5px;box-shadow:0 3px 6px rgba(0,0,0,.2)}
.photo{position:absolute}

/* hero */
.hero{position:absolute;left:0;top:0;width:1200px;height:735px;background:linear-gradient(160deg,#4e5a63 0%,#6c7780 40%,#3b3a38 75%,#2a2826 100%)}
.hero-shade{position:absolute;inset:0;background:rgba(20,25,35,.35)}
.logo{left:77px;top:48px;font:700 16px/1 "Poppins",sans-serif;color:var(--white);letter-spacing:.3px}
.nav{left:379px;top:48px;display:flex;gap:25px;font:400 14px/1 "Roboto",sans-serif;color:#e8e8e8}
.nav .active{color:var(--accent);border-bottom:2px solid var(--accent);padding-bottom:6px}
.nav span{display:flex;align-items:center;gap:5px}
.hero-title{left:575px;top:285px;font:700 30px/1 "Poppins",sans-serif;color:var(--white);letter-spacing:.2px}
.hero-text{left:582px;top:338px;width:560px;font:400 14px/34px "Roboto",sans-serif;color:#f0f0f0}
.hero-curve{position:absolute;left:0;top:660px}

/* about */
.about-title{left:113px;top:855px;font-size:50px}
.about-text{left:111px;top:937px;width:450px;font:300 14px/34px "Roboto",sans-serif;color:#666}
.about-text em{font-style:normal;color:var(--accent)}

/* services */
.services-title{left:0;width:1200px;text-align:center;top:1952px;font-size:50px}
.svc-label{position:absolute;top:2310px;width:318px;text-align:center;font-family:"Amatic SC",sans-serif;font-weight:700;font-size:28px}
.arrow-btn{position:absolute;top:2141px;width:58px;height:58px;border:1px solid #777;border-radius:50%;display:flex;align-items:center;justify-content:center;background:var(--white)}

/* resource */
.res-title{left:640px;top:2610px;font-size:50px}
.res-text{left:644px;top:2673px;width:460px;font:300 14px/34px "Roboto",sans-serif;color:#777}
.res-text p{margin-bottom:10px}
.res-text a{color:var(--accent);text-decoration:underline}

/* contracting */
.con-title{left:113px;top:3130px;font-size:50px}
.view-all{left:1019px;top:3164px;font:700 13px/1 "Roboto",sans-serif;color:var(--navy);text-decoration:underline}
.tile-label{position:absolute;width:100%;text-align:center;color:var(--white);font-family:"Amatic SC",sans-serif;font-weight:700;font-size:24px;text-shadow:0 1px 3px rgba(0,0,0,.5);line-height:34px}

/* extra */
.extra{position:absolute;left:0;top:3941px;width:1200px;height:490px;background:linear-gradient(180deg,#4a4d52,#3a3c40 60%,#4a3a34)}
.extra-title{left:0;width:1200px;text-align:center;top:4058px;font-size:56px;color:var(--white)}
.extra-text{left:110px;top:4135px;width:980px;text-align:center;font:300 14px/34px "Roboto",sans-serif;color:#f2f2f2}

/* footer */
.footer{position:absolute;left:0;top:4431px;width:1200px;height:423px;background:var(--navy)}
.f-head{position:absolute;font:500 16px/1 "Roboto",sans-serif;color:var(--white);letter-spacing:.5px}
.f-head::after{content:"";display:block;width:38px;height:3px;margin-top:8px;border-top:1px solid #9fb2dd;border-bottom:1px solid #9fb2dd}
.f-text{position:absolute;font:400 14px/22px "Roboto",sans-serif;color:#e6ecf8}
.f-list{position:absolute;list-style:none;font:400 14px/1 "Roboto",sans-serif;color:#e6ecf8}
.social{position:absolute;top:4700px;width:44px;height:44px;border:1px solid #e6ecf8;border-radius:50%}
</style>
</head>
<body>

<!-- Hero -->
<section class="hero">
  <div class="hero-bg" role="img" aria-label="Photo of a remodeled bathroom with a soaking tub and glass shower" style="position:absolute;inset:0"></div>
  <div class="hero-shade"></div>
</section>
<div class="abs logo">BRINDLE COVE ABODES.</div>
<nav class="abs nav">
  <span class="active">HOME</span><span>ABOUT US</span><span>PRODUCTS</span><span>EXTRA</span><span>RESOURCE</span><span>CONTACT US</span>
  <span><svg width="11" height="12" viewBox="0 0 11 12"><circle cx="5.5" cy="3.5" r="3" fill="#e8e8e8"/><path d="M0 12c0-4 2.5-5.5 5.5-5.5S11 8 11 12z" fill="#e8e8e8"/></svg>LOGIN</span>
  <span><svg width="12" height="12" viewBox="0 0 24 24"><path fill="#e8e8e8" d="M6.6 10.8a15 15 0 006.6 6.6l2.2-2.2c.3-.3.7-.4 1-.2 1.1.4 2.3.6 3.6.6.6 0 1 .4 1 1V20c0 .6-.4 1-1 1A17 17 0 013 4c0-.6.4-1 1-1h3.5c.6 0 1 .4 1 1 0 1.3.2 2.5.6 3.6.1.3 0 .7-.2 1z"/></svg>615-555-0148</span>
</nav>
<h1 class="abs hero-title">WELCOME TO BRINDLE COVE ABODES.</h1>
<p class="abs hero-text">When you want affordable, quality home construction services; think of us to do the job.</p>
<div class="btn" style="left:582px;top:418px;width:151px;height:49px">Get Started</div>
<svg class="hero-curve" width="1200" height="80" viewBox="0 0 1200 80">
  <path d="M0 75 H500 C540 75 555 20 600 20 C645 20 660 75 700 75 H1200 V80 H0Z" fill="#fff"/>
  <path d="M0 75 H500 C540 75 555 20 600 20 C645 20 660 75 700 75 H1200" fill="none" stroke="#2b4c9a" stroke-width="3"/>
  <path d="M600 34 v18 M592 45 l8 9 8-9" stroke="#888" stroke-width="4" fill="none"/>
</svg>

<!-- About -->
<h2 class="abs display about-title">ABOUT US</h2>
<p class="abs about-text">With over 20 years experience in residential and commercial construction, you can trust your project to Brindle Cove Abodes <em>"DON'T TINKER AROUND"</em> I have built my business with a partnership of clients, employees, subcontractors, suppliers and inspectors. Since each project is unique, this partnership brings creative ideas to your home.</p>
<div class="btn" style="left:111px;top:1162px;width:155px;height:52px">Read More</div>
<div class="photo" role="img" aria-label="Photo of an open living area with polished concrete floor and kitchen beyond" style="left:593px;top:840px;width:500px;height:403px;background:linear-gradient(180deg,#c9cfd2,#9a8f80 55%,#5a4b3a);box-shadow:0 2px 8px rgba(0,0,0,.25)"></div>

<!-- Video band -->
<div class="photo" role="img" aria-label="Photo of a renovated kitchen with stainless fridge and farmhouse sink" style="left:0;top:1345px;width:1200px;height:520px;background:linear-gradient(120deg,#3b4a5c,#6c6f6a 40%,#4a3a30 70%,#2c2a28)"></div>
<svg class="abs" style="left:557px;top:1562px" width="86" height="86" viewBox="0 0 86 86"><circle cx="43" cy="43" r="41" fill="none" stroke="#fff" stroke-width="3"/><path d="M34 27 L60 43 L34 59Z" fill="none" stroke="#fff" stroke-width="3"/></svg>

<!-- Services -->
<h2 class="abs display services-title">SERVICES</h2>
<div class="arrow-btn" style="left:41px"><svg width="12" height="16"><path d="M9 2 L3 8 L9 14" stroke="#333" stroke-width="2" fill="none"/></svg></div>
<div class="arrow-btn" style="left:1098px"><svg width="12" height="16"><path d="M3 2 L9 8 L3 14" stroke="#333" stroke-width="2" fill="none"/></svg></div>
<div class="photo" role="img" aria-label="Photo of a roofer nailing shingles" style="left:111px;top:2042px;width:318px;height:256px;background:linear-gradient(160deg,#8a7a6a,#5a4a44 60%,#3a3230)"></div>
<div class="photo" role="img" aria-label="Photo of a worker installing a window" style="left:441px;top:2042px;width:318px;height:256px;background:linear-gradient(160deg,#e8eef2,#c3ccd4 60%,#3d5e8e)"></div>
<div class="photo" role="img" aria-label="Photo of an electrician working on a panel" style="left:774px;top:2042px;width:315px;height:256px;background:linear-gradient(160deg,#3a4a5a,#6a7a84 60%,#b0a090)"></div>
<div class="svc-label" style="left:111px">ROOFING</div>
<div class="svc-label" style="left:441px">WINDOW REPLACEMENT</div>
<div class="svc-label" style="left:774px">ELECTRICAL</div>
<div class="btn" style="left:522px;top:2394px;width:154px;height:49px">View All</div>

<!-- Resource -->
<div class="abs" style="left:96px;top:2557px;width:499px;height:482px;border:8px solid var(--navy)"></div>
<div class="photo" role="img" aria-label="Photo of a dark wood kitchen with pendant lights" style="left:113px;top:2549px;width:499px;height:484px;background:linear-gradient(170deg,#8a6a4a,#4a3326 45%,#1c1a1a)"></div>
<h2 class="abs display res-title">RESOURCE</h2>
<div class="abs res-text">
  <p>Check out the following links for additional information and helpful resource.</p>
  <p><a>Pictures</a> - Take a look at this link to see a few of the projects we have done recently</p>
  <p><a>Ashford Lumber</a> - Quality products and confident service since 1944</p>
  <p><a>Plumber</a> - Great second generation plumber.</p>
</div>

<!-- Contracting -->
<h2 class="abs display con-title">COMMERCIAL AND RESIDENTIAL CONTRACTING</h2>
<div class="abs view-all">VIEW ALL</div>
<div class="photo" role="img" aria-label="Photo of a sunroom with skylights and brick wall" style="left:0;top:3238px;width:582px;height:600px;background:linear-gradient(170deg,#d8d2c8,#a89278 55%,#6a5444)">
  <div class="tile-label" style="top:218px">PRE CONSTRUCTION CONSULTATION</div></div>
<div class="photo" role="img" aria-label="Photo of blueprints with a hard hat" style="left:599px;top:3238px;width:292px;height:291px;background:linear-gradient(150deg,#c9b070,#d8cfc0 50%,#9a8a70)">
  <div class="tile-label" style="top:40px">NEW CONSTRUCTION</div></div>
<div class="photo" role="img" aria-label="Photo of a white remodeled kitchen" style="left:908px;top:3238px;width:292px;height:291px;background:linear-gradient(160deg,#e8ecef,#b9c0c5 60%,#6a7075)">
  <div class="tile-label" style="top:204px">REMODELING / KITCHENS AND BATHS</div></div>
<div class="photo" role="img" aria-label="Photo of a wooden deck surrounded by trees" style="left:599px;top:3546px;width:292px;height:292px;background:linear-gradient(170deg,#6a8a3a,#4a6a2a 50%,#9a5a3a)">
  <div class="tile-label" style="top:222px">PORCHES AND DECKS</div></div>
<div class="photo" role="img" aria-label="Photo of two contractors reviewing plans in a renovation" style="left:908px;top:3546px;width:292px;height:292px;background:linear-gradient(160deg,#d8d4cc,#9a9088 55%,#5a5048)">
  <div class="tile-label" style="top:190px;padding:0 10px 0 90px;text-align:right">SPECIALIZING IN HISTORIC RENOVATIONS.</div></div>

<!-- Extra -->
<div class="extra" role="img" aria-label="Photo of homes under construction with a crane"></div>
<h2 class="abs display extra-title">EXTRA</h2>
<p class="abs extra-text">When you view your home as your castle, you appreciate craftsmen working on it with a sense of respect.When the light goes on for a better idea we want to be there to enjoy it too! Since Brindle Cove Abodes is in Nashville, Tennessee we are constantly working with time proven architectural ideas, as well as, new influences that come to Nashville from other parts of the country.</p>
<div class="btn" style="left:524px;top:4258px;width:152px;height:49px">Contact Us</div>

<!-- Footer -->
<footer class="footer"></footer>
<div class="abs" style="left:111px;top:4518px;font:700 16px/1 'Poppins',sans-serif;color:#fff">BRINDLE COVE ABODES.</div>
<p class="f-text" style="left:111px;top:4566px;width:270px;font-size:11px;line-height:27px">With over 20 years experience in residential and commercial construction, you can trust your project to Brindle Cove Abodes</p>
<div class="abs" style="left:111px;top:4680px;font:500 16px/1 'Roboto',sans-serif;color:#fff">FOLLOW US</div>
<div class="social" style="left:113px;top:4722px"></div>
<div class="social" style="left:165px;top:4722px"></div>
<div class="social" style="left:217px;top:4722px"></div>
<div class="abs" style="left:414px;top:4500px;width:1px;height:265px;background:#6f88c2"></div>

<div class="f-head" style="left:477px;top:4512px">CONTACT US</div>
<div class="f-text" style="left:484px;top:4560px">&#9990; 615-555-0148</div>
<div class="f-text" style="left:484px;top:4602px;width:180px">&#9679; 42 Placeholder Lane, Suite 7</div>
<div class="f-text" style="left:484px;top:4680px;width:190px">&#9993; walter@brindlecove abodes.com</div>

<div class="f-head" style="left:718px;top:4512px">SERVICES</div>
<ul class="f-list" style="left:724px;top:4563px;line-height:43px">
  <li>&raquo; Pre Construction Consultation</li><li>&raquo; New Construction</li><li>&raquo; Additions</li><li>&raquo; Porches and Decks</li>
</ul>

<div class="f-head" style="left:1004px;top:4512px">LINKS</div>
<ul class="f-list" style="left:1011px;top:4563px;line-height:33px">
  <li>Home</li><li>About Us</li><li>Products</li><li>Extra</li><li>Resource</li><li>Contact Us</li>
</ul>
<div class="abs" style="left:885px;top:4795px;width:200px;text-align:right;font:400 14px/1 'Roboto',sans-serif;color:#e6ecf8">&copy; 2021 All Rights Reserved</div>

</body>
</html>
```